Business card design reauest

2 sided. White on both sides

Martin Oakhurst

Ho Chi Minh, Vietnam

Cell Phone / Whatsapp/ Wechat/Zalo
1-555-382-7194
Moakhurst@kvpartsline.vn
Www.kvpartsline.vn
Www.kvpartsline.com

Industry/Entity Type

Sofa and furniture and kitchen

Contact Information for Business Card

2 sided. White on both sides Martin Oakhurst Ho Chi Minh, Vietnam Cell Phone / Whatsapp/ Wechat/Zalo 1-555-382-7194 Moakhurst@kvpartsline.vn Www.kvpartsline.vn Www.kvpartsline.com

```html
<!DOCTYPE html>
<html lang="en">
<head>
<meta charset="utf-8">
<title>KV Parts Line – Business Card</title>
<link href="https://fonts.googleapis.com/css2?family=Marcellus&family=Lato:wght@400&display=swap" rel="stylesheet">
<style>
  :root {
    --stage: #333333;
    --brand-green: #0f9a48;
    --ink: #1c1c1c;
    --muted: #3a3a3a;
    --silver-light: #fbfbfb;
    --silver-mid: #e2e2e2;
    --silver-dark: #c9c9c9;
  }
  * { margin: 0; padding: 0; box-sizing: border-box; }
  html, body { width: 1200px; height: 1000px; overflow: hidden; }
  body { background: var(--stage); position: relative; font-family: "Lato", Arial, sans-serif; }

  .card {
    position: absolute;
    left: 185px;
    width: 828px;
    height: 472px;
    background:
      linear-gradient(115deg, var(--silver-dark) 0%, var(--silver-light) 18%, var(--silver-mid) 34%, var(--silver-light) 55%, var(--silver-dark) 72%, var(--silver-light) 88%, var(--silver-mid) 100%);
  }
  .card--front { top: 20px; }
  .card--back { top: 507px; }

  .brand {
    position: absolute;
    display: flex;
    align-items: center;
    gap: 22px;
    font-family: "Marcellus", Georgia, serif;
    color: var(--brand-green);
    text-transform: uppercase;
    white-space: nowrap;
  }
  .brand__square { background: var(--brand-green); flex: none; }

  .card--front .brand { left: 0; right: 0; top: 180px; justify-content: center; font-size: 46px; letter-spacing: 1px; }
  .card--front .brand__square { width: 76px; height: 76px; }

  .website-line {
    position: absolute;
    left: 0; right: 0; top: 398px;
    display: flex; justify-content: center; align-items: center; gap: 10px;
    font-size: 21px; color: var(--ink);
  }
  .website-line::before, .website-line::after {
    content: ""; width: 18px; height: 3px; background: var(--brand-green);
  }

  .card--back .brand { left: 0; right: 0; top: 160px; justify-content: center; font-size: 32px; letter-spacing: 1px; gap: 14px; }
  .card--back .brand__square { width: 46px; height: 46px; }

  .holder { position: absolute; left: 95px; top: 355px; width: 263px; text-align: center; }
  .holder__name { font-family: "Marcellus", Georgia, serif; color: var(--brand-green); font-size: 30px; text-transform: uppercase; letter-spacing: 0.5px; line-height: 1.1; white-space: nowrap; }
  .holder__place { font-size: 18px; color: var(--muted); margin-top: 8px; }

  .divider { position: absolute; left: 403px; top: 345px; width: 2px; height: 96px; background: var(--brand-green); }

  .contacts { position: absolute; left: 454px; top: 345px; list-style: none; }
  .contacts li { display: flex; align-items: center; gap: 8px; height: 29.5px; font-size: 21px; color: var(--ink); }
  .contacts svg { width: 17px; height: 17px; fill: var(--brand-green); flex: none; }
</style>
</head>
<body>
  <section class="card card--front">
    <div class="brand"><span class="brand__square"></span><span class="brand__name">KV Parts Line</span></div>
    <p class="website-line">www.kvpartsline.com</p>
  </section>

  <section class="card card--back">
    <div class="brand"><span class="brand__square"></span><span class="brand__name">KV Parts Line</span></div>

    <div class="holder">
      <p class="holder__name">Martin Oakhurst</p>
      <p class="holder__place">Ho Chi Minh, Vietnam</p>
    </div>

    <div class="divider"></div>

    <ul class="contacts">
      <li>
        <svg viewBox="0 0 24 24" aria-hidden="true"><path d="M6.6 10.8a15.1 15.1 0 0 0 6.6 6.6l2.2-2.2c.3-.3.7-.4 1-.2 1.1.4 2.3.6 3.6.6.6 0 1 .4 1 1V20c0 .6-.4 1-1 1A17 17 0 0 1 3 4c0-.6.4-1 1-1h3.5c.6 0 1 .4 1 1 0 1.3.2 2.5.6 3.6.1.3 0 .7-.2 1z"/></svg>
        <span>1-555-382-7194</span>
      </li>
      <li>
        <svg viewBox="0 0 24 24" aria-hidden="true"><path d="M22 2 2 10.5l7 2.5 2.5 7L22 2zM9.8 12.2 18 6l-6.2 8.2-.6 3.2z"/></svg>
        <span>Moakhurst@kvpartsline.vn</span>
      </li>
      <li>
        <svg viewBox="0 0 24 24" aria-hidden="true"><path d="M12 2a10 10 0 1 0 0 20 10 10 0 0 0 0-20zm6.9 6h-3a15 15 0 0 0-1.3-3.9A8 8 0 0 1 18.9 8zM12 4c.8 1.2 1.5 2.5 1.9 4h-3.8c.4-1.5 1.1-2.8 1.9-4zM4.3 14a8 8 0 0 1 0-4h3.4a16 16 0 0 0 0 4zm.8 2h3a15 15 0 0 0 1.3 3.9A8 8 0 0 1 5.1 16zm3-8h-3a8 8 0 0 1 4.3-3.9A15 15 0 0 0 8.1 8zM12 20c-.8-1.2-1.5-2.5-1.9-4h3.8c-.4 1.5-1.1 2.8-1.9 4zm2.3-6H9.7a14 14 0 0 1 0-4h4.6a14 14 0 0 1 0 4zm.3 5.9a15 15 0 0 0 1.3-3.9h3a8 8 0 0 1-4.3 3.9zm1.7-5.9a16 16 0 0 0 0-4h3.4a8 8 0 0 1 0 4z"/></svg>
        <span>www.kvpartsline.vn</span>
      </li>
    </ul>
  </section>
</body>
</html>
```